Carpet cleaning company wants business card

Need an exciting new fresh design for business cards for my carpet cleaning /pest control business
www.tidewellhomecare.com.au
Can design include a lined section for quoting or information? Thanks !

```html
<!DOCTYPE html>
<html lang="en">
<head>
<meta charset="utf-8">
<title>Tidewell Home Care – Business Card</title>
<link href="https://fonts.googleapis.com/css2?family=Lato:wght@400;700;900&display=swap" rel="stylesheet">
<style>
  :root {
    --brand-blue: #0756a8;
    --brand-red: #e8333a;
    --ink-grey: #5a5a5a;
    --paper: #ffffff;
    --backdrop: #2a2b2e;
    --rule: #e2e2e2;
  }
  * { box-sizing: border-box; margin: 0; padding: 0; }
  html, body { width: 1200px; height: 952px; overflow: hidden; }
  body {
    background: var(--backdrop);
    font-family: "Lato", sans-serif;
    display: flex;
    align-items: center;
    justify-content: center;
    gap: 48px;
  }
  .card {
    position: relative;
    width: 520px;
    height: 300px;
    overflow: hidden;
    box-shadow: 0 10px 30px rgba(0,0,0,0.45);
  }

  /* Front */
  .card-front {
    background: var(--brand-blue);
    display: flex;
    align-items: center;
    justify-content: center;
  }
  .front-wordmark {
    display: flex;
    align-items: center;
    gap: 14px;
    color: var(--paper);
    font-weight: 900;
    font-size: 40px;
    letter-spacing: -0.5px;
  }
  .front-wordmark .mark-square {
    width: 26px; height: 26px;
    background: var(--brand-red);
  }

  /* Back */
  .card-back { background: var(--paper); }
  .edge-bar { position: absolute; background: var(--brand-blue); }
  .edge-bar.left { left: 0; top: 52px; width: 12px; height: 108px; }
  .edge-bar.right { right: 0; top: 178px; width: 14px; height: 96px; }

  .back-wordmark {
    position: absolute;
    left: 36px; top: 96px;
    color: var(--brand-blue);
    font-weight: 900;
    font-size: 21px;
    letter-spacing: -0.3px;
  }
  .divider { position: absolute; left: 0; top: 0; }

  .contact-block {
    position: absolute;
    left: 292px; top: 92px;
  }
  .person-name {
    font-size: 19px;
    font-weight: 400;
    color: var(--brand-red);
    letter-spacing: 0.5px;
    text-transform: uppercase;
  }
  .person-name .surname { color: var(--brand-blue); font-weight: 900; }
  .person-role { font-size: 13px; color: var(--ink-grey); margin-top: 2px; }
  .contact-list { list-style: none; margin-top: 12px; }
  .contact-list li {
    display: flex; align-items: center; gap: 7px;
    font-size: 11.5px; color: var(--ink-grey);
    line-height: 19px;
  }
  .contact-list svg { width: 10px; height: 10px; fill: var(--brand-red); flex: none; }
  .address {
    position: absolute;
    left: 36px; bottom: 30px;
    font-size: 11px;
    color: var(--ink-grey);
  }
</style>
</head>
<body>
  <section class="card card-front" aria-label="Card front">
    <div class="front-wordmark"><span class="mark-square"></span>Tidewell Home Care</div>
  </section>

  <section class="card card-back" aria-label="Card back">
    <span class="edge-bar left"></span>
    <span class="edge-bar right"></span>
    <div class="back-wordmark">Tidewell Home Care</div>
    <svg class="divider" width="520" height="300" aria-hidden="true">
      <line x1="290" y1="60" x2="250" y2="190" stroke="var(--rule)" stroke-width="1"/>
    </svg>
    <div class="contact-block">
      <p class="person-name">Daniel M. <span class="surname">Harlow</span></p>
      <p class="person-role">Managing Director</p>
      <ul class="contact-list">
        <li><svg viewBox="0 0 10 10"><path d="M2 0h2l1 3-1.5 1a6 6 0 0 0 2.5 2.5L7 5l3 1v2c0 1-1 2-2 2A8 8 0 0 1 0 2c0-1 1-2 2-2z"/></svg>+00 987 654 32</li>
        <li><svg viewBox="0 0 10 10"><path d="M0 2h10v6H0zM0 2l5 3.5L10 2" stroke="#fff" stroke-width="0.8"/></svg>hello@tidewellmail.com</li>
        <li><svg viewBox="0 0 10 10"><circle cx="5" cy="5" r="5"/><path d="M0 5h10M5 0c-2 3-2 7 0 10M5 0c2 3 2 7 0 10" stroke="#fff" stroke-width="0.8" fill="none"/></svg>www.tidewellhomecare.com.au</li>
      </ul>
    </div>
    <p class="address">4120 Riverside Avenue Lakeport, DC 20031</p>
  </section>
</body>
</html>
```